Harbor Healthcare Coming Soon Sign

I need a large (10 x5) road banner announcing the construction of our new medical practice at 5817 Marlow Creek Road in John's Island. The name of our practice is Harbor Healthcare and we thought it would be fund to nick name it the "Harbor Lookout". We'd like the tagline to read - "There's nothing healthy about driving an hour to see your doctor. So we're coming to you." Opening Late 2025 I have attached three logos as we have two other practices (Harbor Urgent and Harbor Aesthetics ) that should be present on the bottom of the sign but the main business is Harbor Healthcare. For more information on our look/feel visit our website www.wekeepitplain.example (which should be somewhere on the banner as well)
Updates

The signage needs to say Coming Late Fall 2025!

Target Market(s)

Drive By traffic must be made aware that we are coming soon

Industry/Entity Type

Healthcare

Requirements
Nice to have
• Western Theme

```html
<!DOCTYPE html>
<html lang="en">
<head>
<meta charset="utf-8">
<title>Harbor Healthcare – Coming Late Fall 2025</title>
<link rel="stylesheet" href="https://fonts.googleapis.com/css2?family=Rye&family=Cinzel:wght@900&family=Poppins:wght@600;700&family=Oswald:wght@600&display=swap">
<style>
  :root {
    --page: #8a8a8a;
    --navy: #0d2a66;
    --navy-deep: #071a45;
    --navy-mid: #1a4a98;
    --sky: #7cc2ee;
    --sky-dark: #123a78;
    --gold: #f2ad2e;
    --gold-band: #f0aa2a;
    --white: #ffffff;
    --ink: #0c1f4a;
    --pink: #e8197f;
    --blue-brand: #6ab7e6;
    --red: #e8382f;
    --line: rgba(255,255,255,0.35);
  }
  * { box-sizing: border-box; margin: 0; padding: 0; }
  html, body { width: 1200px; height: 807px; overflow: hidden; background: var(--page); }
  .banner {
    position: absolute; left: 20px; top: 113px; width: 1160px; height: 580px;
    background: radial-gradient(ellipse at 50% 40%, var(--navy-mid) 0%, var(--navy) 55%, var(--navy-deep) 100%);
    overflow: hidden;
  }
  .decor { position: absolute; border-radius: 24px; background: rgba(255,255,255,0.05); }
  .decor-clipboard { left: 115px; top: 0; width: 110px; height: 80px; transform: rotate(-15deg); }
  .decor-heart { right: 80px; top: 30px; width: 130px; height: 110px; border-radius: 50%; }
  .decor-stethoscope { left: 0; top: 200px; width: 110px; height: 130px; border-radius: 50%; }
  .decor-kit { right: 0; top: 200px; width: 90px; height: 110px; }
  .headline { position: absolute; inset: 0; width: 1160px; height: 380px; }
  .coming { font-family: "Rye", serif; font-size: 50px; fill: var(--gold); }
  .arch-title {
    font-family: "Rye", serif; font-size: 132px; fill: var(--sky);
    stroke: var(--sky-dark); stroke-width: 3; paint-order: stroke;
  }
  .tagline { font-family: "Oswald", sans-serif; font-weight: 600; font-size: 30px; fill: var(--gold); letter-spacing: -0.5px; }
  .subline { font-family: "Cinzel", serif; font-weight: 900; font-size: 34px; fill: var(--white); }
  .web-band {
    position: absolute; left: 0; top: 380px; width: 100%; height: 60px;
    background: var(--gold-band);
    display: flex; align-items: center; justify-content: center;
  }
  .web-address {
    font-family: "Poppins", sans-serif; font-weight: 700; font-size: 33px;
    letter-spacing: 3px; color: var(--ink);
  }
  .brands {
    position: absolute; left: 0; top: 440px; width: 100%; height: 140px;
    display: flex; align-items: center; justify-content: space-around; padding: 0 30px;
  }
  .brand { display: flex; align-items: center; gap: 16px; }
  .brand-mark { width: 54px; height: 54px; border-radius: 50%; }
  .brand-name {
    font-family: "Poppins", sans-serif; font-weight: 600; font-size: 26px;
    line-height: 1.15; letter-spacing: 4px; text-transform: uppercase;
  }
  .brand--aesthetics .brand-mark { background: var(--pink); }
  .brand--aesthetics .brand-name { color: var(--pink); }
  .brand--healthcare .brand-mark { background: var(--blue-brand); border-radius: 10px; width: 70px; height: 70px; }
  .brand--healthcare .brand-name { color: var(--blue-brand); font-size: 32px; }
  .brand--urgent .brand-mark { background: var(--red); border-radius: 8px; }
  .brand--urgent .brand-name { color: var(--red); }
  .divider { width: 0; height: 74px; border-left: 1px dashed var(--line); }
</style>
</head>
<body>
  <main class="banner">
    <div class="decor decor-clipboard" role="img" aria-label="Faint line drawing of a medical clipboard"></div>
    <div class="decor decor-heart" role="img" aria-label="Faint line drawing of a heart with a heartbeat line"></div>
    <div class="decor decor-stethoscope" role="img" aria-label="Faint line drawing of a stethoscope"></div>
    <div class="decor decor-kit" role="img" aria-label="Faint line drawing of a medical kit"></div>

    <svg class="headline" viewBox="0 0 1160 380" aria-label="Coming Late Fall 2025">
      <defs>
        <path id="title-arch" d="M 120 305 Q 580 125 1075 305"/>
      </defs>
      <text class="coming" x="580" y="92" text-anchor="middle">COMING</text>
      <text class="arch-title">
        <textPath href="#title-arch" startOffset="50%" text-anchor="middle" textLength="960" lengthAdjust="spacingAndGlyphs">LATE FALL 2025</textPath>
      </text>
      <text class="tagline" x="580" y="305" text-anchor="middle">CONSERVING RURAL JOHN'S ISLAND WITH</text>
      <text class="subline" x="580" y="355" text-anchor="middle" textLength="870" lengthAdjust="spacingAndGlyphs">HOME GROWN PROGRESSIVE PRIMARY CARE</text>
    </svg>

    <div class="web-band">
      <span class="web-address">www.harborhealthcarecoast.example</span>
    </div>

    <div class="brands">
      <div class="brand brand--aesthetics">
        <span class="brand-mark"></span>
        <span class="brand-name">Harbor<br>Aesthetics</span>
      </div>
      <span class="divider"></span>
      <div class="brand brand--healthcare">
        <span class="brand-mark"></span>
        <span class="brand-name">Harbor<br>Healthcare</span>
      </div>
      <span class="divider"></span>
      <div class="brand brand--urgent">
        <span class="brand-mark"></span>
        <span class="brand-name">Harbor<br>Urgent</span>
      </div>
    </div>
  </main>
</body>
</html>
```